Federal IT Consulting Company - Bridgemont Consulting Group

We're seeking a skilled web designer to create a modern, bold, and engaging WordPress website for Bridgemont Consulting Group, LLC. Our company specializes in federal IT consulting, and our name is a play on "Bridging Momentum." The website should reflect our expertise in the federal technology marketplace and position us as a trusted partner for clients navigating their IT journey.

contact: info@bridgemontgrp.com

Current Status

WordPress is already installed on our hosting account
We have an existing logo (may need modernization)

Design Requirements

Style:

Modern and visually striking design
Bold elements to convey confidence and expertise
Incorporate the concept of "bridging momentum" into the design

Features:

Modern UX sliders for dynamic content presentation
Eye-catching, high-quality images (stock photos to be sourced by the designer)
Responsive design for all devices

Color Scheme:

To be proposed by the designer, should align with our brand and convey trust and technological expertise

Logo:

Evaluate our current logo
Create a transparent background version if needed
Propose modernization if deemed necessary

Accessibility:

Ensure design elements are accessible to users with disabilities
Use high contrast ratios for text and background colors
Provide text alternatives for non-text content

Website Structure
Create the following pages, with the possibility of subpages:

Home
Services
About
Contact

Specific Page Requirements
Home Page

Striking hero section with a clear value proposition
Overview of our services
Client testimonials or trust indicators

Services Page

Detailed list of our IT consulting services
Clear explanation of how we help navigate the federal IT landscape

About Page

Company history and mission
Team highlights (if applicable)
Our approach to federal IT consulting

Contact Page

Contact form
Other contact methods (phone, email)

Technical Requirements

Fully responsive design
SEO best practices implemented
Fast loading times
Integration with necessary plugins (to be discussed)
Training on how to update and maintain the site
Full compliance with Web Content Accessibility Guidelines (WCAG) 2.1 Level AA
Adherence to Section 508 standards for federal website accessibility
Implementation of necessary features for ADA compliance
Updates

Designs look the same

Target Market(s)

US Federal Govt customers looking for IT support.

Industry/Entity Type

IT Consulting

Coding

Coded - Design and coding required

Colors
0054AA
0677BA
7BADD7
CADEEF
E8F1F8
0094D4
00A9DD
6FCCEA
C7EBF8
E9F6FB
00AB8E
00BBA5
67D7C9
C6EFE9
E9F9F6

```html
<!DOCTYPE html>
<html lang="en">
<head>
<meta charset="utf-8">
<title>Bridgemont Consulting Group</title>
<link href="https://fonts.googleapis.com/css2?family=Poppins:wght@300;400;500;600;700&display=swap" rel="stylesheet">
<style>
:root{
  --cyan:#0aa2dc;
  --cyan-dark:#0094d4;
  --cyan-pale:#e9f6fb;
  --navy:#07115e;
  --navy-deep:#030a45;
  --ink:#1d1d1f;
  --body:#333;
  --soft:#f4f4f4;
  --line:#cfe7f2;
  --footer:#3a3a3c;
  --white:#fff;
}
*{box-sizing:border-box;margin:0;padding:0}
html,body{width:1200px;height:5042px;overflow:hidden}
body{position:relative;font-family:'Poppins',sans-serif;color:var(--body);background:var(--white)}
section,header,footer{position:absolute;left:0;width:1200px}

/* header */
.site-header{top:0;height:127px;background:var(--white)}
.brand{position:absolute;left:74px;top:44px;display:flex;align-items:center;gap:12px;font-weight:700;font-size:30px;color:var(--navy);letter-spacing:1px}
.brand-dot{width:34px;height:34px;border-radius:50%;background:var(--cyan)}
.nav{position:absolute;top:41px;left:0;width:1200px;height:37px}
.nav a{position:absolute;top:10px;font-size:13px;color:#444;text-decoration:none}
.nav a.active{color:var(--cyan)}
.nav .nav-cta{top:0;left:1033px;width:92px;height:37px;border-radius:19px;background:var(--cyan);color:#fff;display:flex;align-items:center;justify-content:center}

/* hero */
.hero{top:127px;height:721px;background:radial-gradient(ellipse at 70% 45%,#10208a 0%,var(--navy) 45%,var(--navy-deep) 100%)}
.hero-art{position:absolute;left:600px;top:65px;width:600px;height:630px;background:linear-gradient(150deg,#1a6fd8 0%,#0b3aa8 50%,#07186a 100%);clip-path:polygon(50% 0,100% 22%,100% 72%,50% 100%,0 72%,0 22%);opacity:.9}
.hero-copy{position:absolute;left:0;top:0;width:580px;height:721px;z-index:2}
.hero-welcome{position:absolute;left:69px;top:180px;font-size:30px;color:#1fb6ec}
.hero-title{position:absolute;left:68px;top:222px;font-size:66px;font-weight:700;color:#fff;letter-spacing:1px;line-height:1;white-space:nowrap}
.hero-text{position:absolute;left:78px;top:322px;width:440px;font-size:16.5px;line-height:24px;color:#fff}
.btn{position:absolute;display:flex;align-items:center;justify-content:center;gap:14px;border-radius:30px;font-size:17px;text-decoration:none}
.btn-solid{background:var(--cyan);color:#fff}
.btn-outline{border:2px solid #fff;color:#fff}
.hero .btn{left:72px;top:421px;width:206px;height:59px}

/* section headings */
.heading{position:absolute;left:0;width:1200px;text-align:center}
.heading-inner{display:inline-block;text-align:right}
.heading-title{display:block;font-size:44px;font-weight:600;color:var(--ink);white-space:nowrap;line-height:1.1}
.heading-sub{display:block;margin-top:6px;font-size:23px;font-weight:600;color:var(--cyan);letter-spacing:3px;white-space:nowrap;line-height:1}

/* services */
.services{top:848px;height:992px;background:var(--soft)}
.svc{position:absolute;text-align:center}
.svc.featured{background:var(--cyan)}
.svc-icon{position:absolute;left:50%;transform:translateX(-50%);width:96px;height:96px;border-radius:50%;background:var(--cyan-pale);display:flex;align-items:center;justify-content:center}
.svc.featured .svc-icon{background:rgba(255,255,255,.18)}
.svc-title{position:absolute;left:0;width:100%;font-size:16px;color:var(--cyan);letter-spacing:.5px}
.svc.featured .svc-title,.svc.featured .svc-text{color:#fff}
.svc-text{position:absolute;left:50%;transform:translateX(-50%);width:240px;font-size:12.5px;line-height:23px;color:#444}
.grid-line{position:absolute;background:var(--line)}

/* why choose */
.why{top:1840px;height:760px;background:#fff}
.why-photo{position:absolute;left:407px;top:401px;width:397px;height:239px;border-radius:200px 200px 0 0;background:linear-gradient(180deg,#45505e 0%,#27313f 60%,#2a3a52 100%)}
.why-halo{position:absolute;left:380px;top:310px;width:450px;height:330px;border-radius:225px 225px 0 0;background:radial-gradient(circle at 50% 100%,#e9f6fb 0%,#fff 70%)}
.why-item{position:absolute;width:98px;height:98px;border-radius:50%;background:var(--cyan);border:5px solid #fff;box-shadow:0 0 0 2px var(--cyan);display:flex;align-items:center;justify-content:center}
.why-label{position:absolute;font-size:18px;color:var(--ink);white-space:nowrap}

/* about */
.about{top:2600px;height:688px;background:#fff}
.about-photo{position:absolute;left:515px;top:0;width:685px;height:688px;background:linear-gradient(160deg,#c8d2dc 0%,#5d6877 40%,#2c3440 65%,#dfe8f0 100%)}
.about-card{position:absolute;left:0;top:48px;width:622px;height:538px;background:#fff;border-radius:0 18px 18px 0;box-shadow:0 4px 30px rgba(0,0,0,.08)}
.about-heading{position:absolute;right:60px;top:148px;text-align:right}
.about-text{position:absolute;left:137px;top:282px;width:425px;font-size:13px;line-height:23px;text-align:right;color:#333}
.about .btn{left:362px;top:417px;width:204px;height:59px}

/* cta */
.cta{top:3288px;height:512px;background:linear-gradient(90deg,#0d9bd6 0%,#1fb0e6 55%,#18a6de 100%);text-align:center;color:#fff}
.cta h2{position:absolute;left:0;width:1200px;top:112px;font-size:40px;font-weight:600}
.cta h3{position:absolute;left:0;width:1200px;top:176px;font-size:24px;font-weight:400}
.cta p{position:absolute;left:150px;width:900px;top:240px;font-size:13px;line-height:23px}
.cta .btn{left:530px;top:362px;width:208px;height:59px}

/* testimonials */
.testimonials{top:3800px;height:790px;background:#fff}
.t-card{position:absolute;top:373px;width:316px;height:244px;background:#fff;border:1px solid #e4e4e4;border-bottom:5px solid var(--cyan);border-radius:8px;box-shadow:0 3px 10px rgba(0,0,0,.08)}
.t-avatar{position:absolute;left:30px;top:-32px;width:66px;height:66px;border-radius:50%;background:linear-gradient(135deg,#d8c4b6,#8a7a70);border:3px solid #fff}
.t-quote{position:absolute;right:30px;top:18px;font-size:110px;line-height:1;color:#e4e4e4;font-family:Georgia,serif}
.t-text{position:absolute;left:34px;top:62px;width:248px;font-size:13px;line-height:22px;text-align:justify;color:#444}
.t-rule{position:absolute;left:34px;right:34px;top:180px;height:1px;background:#ddd}
.t-name{position:absolute;left:34px;top:186px;font-size:12px;font-weight:600;color:var(--ink)}
.t-role{position:absolute;left:34px;top:202px;font-size:9px;color:#777}
.t-stars{position:absolute;right:34px;top:186px;font-size:12px;color:#f5b301;letter-spacing:1px}
.dot{position:absolute;top:695px;width:12px;height:12px;border-radius:50%;background:#c7ebf8}
.dot.on{background:var(--cyan)}

/* footer */
.site-footer{top:4590px;height:392px;background:var(--footer);color:#fff}
.f-brand{position:absolute;left:70px;top:183px;display:flex;align-items:center;gap:10px;font-size:28px;font-weight:700;letter-spacing:1px}
.f-brand .brand-dot{width:30px;height:30px}
.f-social{position:absolute;top:289px;width:28px;height:28px;border:1px solid var(--cyan);border-radius:3px}
.f-title{position:absolute;top:120px;font-size:15px;color:var(--cyan);letter-spacing:.5px}
.f-title::after{content:"";position:absolute;left:0;top:26px;width:32px;height:2px;background:var(--cyan)}
.f-links{position:absolute;left:395px;top:187px;list-style:none;font-size:13px;line-height:27px}
.f-links li::before{content:"";display:inline-block;width:8px;height:8px;border:1px solid var(--cyan);border-radius:50%;margin-right:4px;border-right-color:transparent}
.f-contact{position:absolute;left:603px;font-size:12px;line-height:16px;display:flex;gap:18px}
.f-ico{width:26px;height:26px;border-radius:50%;border:1px solid var(--cyan);display:flex;align-items:center;justify-content:center;flex:none}
.f-news{position:absolute;left:894px;top:185px;width:220px;font-size:12px;line-height:18px}
.f-input{position:absolute;left:886px;top:246px;width:208px;height:33px;border:1px solid var(--cyan);border-radius:17px;font-size:11px;color:#aaa;padding:8px 16px}
.f-input span{position:absolute;right:4px;top:4px;width:23px;height:23px;border-radius:50%;border:1px solid var(--cyan)}
.copyright{position:absolute;left:0;top:4982px;width:1200px;height:60px;background:var(--cyan);color:#fff;font-size:11px;text-align:center;line-height:60px}
</style>
</head>
<body>

<header class="site-header">
  <div class="brand"><span class="brand-dot"></span>BRIDGEMONT</div>
  <nav class="nav">
    <a class="active" style="left:715px">HOME</a>
    <a style="left:789px">SERVICES</a>
    <a style="left:885px">ABOUT</a>
    <a style="left:967px">BLOG</a>
    <a class="nav-cta">CONTACT</a>
  </nav>
</header>

<section class="hero">
  <div class="hero-art" role="img" aria-label="Isometric illustration of a team meeting in a room with data dashboards on the walls"></div>
  <div class="hero-copy">
    <div class="hero-welcome">Welcome to</div>
    <h1 class="hero-title">BRIDGEMONT</h1>
    <p class="hero-text">Lorem ipsum dolor sit amet, consectetur adipiscing elit, sed do eiusmod tempor incididunt</p>
    <a class="btn btn-solid">GET STARTED
      <svg width="30" height="14" viewBox="0 0 30 14"><path d="M0 7h27M21 1l6 6-6 6" stroke="#fff" stroke-width="2" fill="none"/></svg></a>
  </div>
</section>

<section class="services">
  <div class="heading" style="top:126px"><div class="heading-inner">
    <span class="heading-title">OUR SERVICES</span>
    <span class="heading-sub">WHAT WE DO</span>
  </div></div>

  <div class="svc featured" style="left:427px;top:295px;width:344px;height:300px"></div>
  <div class="grid-line" style="left:98px;top:595px;width:1014px;height:2px"></div>
  <div class="grid-line" style="left:427px;top:595px;width:2px;height:293px"></div>
  <div class="grid-line" style="left:771px;top:595px;width:2px;height:293px"></div>

  <div class="svc" style="left:98px;top:295px;width:329px;height:300px">
    <div class="svc-icon" style="top:34px"><svg width="36" height="30" viewBox="0 0 36 30"><rect x="1" y="1" width="34" height="28" rx="2" stroke="#0aa2dc" stroke-width="2.5" fill="none"/><path d="M1 8h34M13 14l-4 4 4 4M23 14l4 4-4 4" stroke="#0aa2dc" stroke-width="2.5" fill="none"/></svg></div>
    <div class="svc-title" style="top:148px">APPLICATION DESIGN</div>
    <p class="svc-text" style="top:188px">Lorem ipsum dolor sit amet, conse ctetur adipiscing elit, sed do eiusmod tempor</p>
  </div>
  <div class="svc featured" style="left:427px;top:295px;width:344px;height:300px">
    <div class="svc-icon" style="top:34px"><svg width="36" height="32" viewBox="0 0 36 32"><path d="M9 22a7 7 0 0 1 1-14 9 9 0 0 1 17 2 6 6 0 0 1 0 12z" stroke="#fff" stroke-width="2.5" fill="none"/><path d="M18 22v8M10 30h16" stroke="#fff" stroke-width="2.5"/></svg></div>
    <div class="svc-title" style="top:148px">WEB HOSTING</div>
    <p class="svc-text" style="top:188px">Lorem ipsum dolor sit amet, conse ctetur adipiscing elit, sed do eiusmod tempor</p>
  </div>
  <div class="svc" style="left:771px;top:295px;width:341px;height:300px">
    <div class="svc-icon" style="top:34px"><svg width="34" height="34" viewBox="0 0 34 34"><circle cx="17" cy="17" r="7" stroke="#0aa2dc" stroke-width="2.5" fill="none"/><path d="M17 3v6M17 25v6M3 17h6M25 17h6" stroke="#0aa2dc" stroke-width="2.5"/></svg></div>
    <div class="svc-title" style="top:148px">APPLICATION DESIGN</div>
    <p class="svc-text" style="top:188px">Lorem ipsum dolor sit amet, conse ctetur adipiscing elit, sed do eiusmod tempor</p>
  </div>

  <div class="svc" style="left:98px;top:597px;width:329px;height:291px">
    <div class="svc-icon" style="top:52px"><svg width="34" height="34" viewBox="0 0 34 34"><circle cx="17" cy="17" r="13" stroke="#0aa2dc" stroke-width="2.5" fill="none"/><path d="M11 17l4 4 8-8" stroke="#0aa2dc" stroke-width="2.5" fill="none"/></svg></div>
    <div class="svc-title" style="top:177px">SEO OPTIMIZATION</div>
    <p class="svc-text" style="top:216px">Lorem ipsum dolor sit amet, conse ctetur adipiscing elit, sed do eiusmod tempor</p>
  </div>
  <div class="svc" style="left:429px;top:597px;width:342px;height:291px">
    <div class="svc-icon" style="top:52px"><svg width="34" height="34" viewBox="0 0 34 34"><path d="M4 30V18M12 30V10M20 30V14M28 30V5" stroke="#0aa2dc" stroke-width="3"/></svg></div>
    <div class="svc-title" style="top:177px">DIGITAL MARKETING</div>
    <p class="svc-text" style="top:216px">Lorem ipsum dolor sit amet, conse ctetur adipiscing elit, sed do eiusmod tempor</p>
  </div>
  <div class="svc" style="left:773px;top:597px;width:339px;height:291px">
    <div class="svc-icon" style="top:52px"><svg width="30" height="34" viewBox="0 0 30 34"><rect x="3" y="14" width="24" height="18" rx="2" stroke="#0aa2dc" stroke-width="2.5" fill="none"/><path d="M8 14V9a7 7 0 0 1 14 0v5" stroke="#0aa2dc" stroke-width="2.5" fill="none"/></svg></div>
    <div class="svc-title" style="top:177px">DATA SECURITY</div>
    <p class="svc-text" style="top:216px">Lorem ipsum dolor sit amet, conse ctetur adipiscing elit, sed do eiusmod tempor</p>
  </div>
</section>

<section class="why">
  <div class="heading" style="top:146px"><div class="heading-inner">
    <span class="heading-title">WHY CHOOSE</span>
    <span class="heading-sub">BRIDGEMONT</span>
  </div></div>

  <div class="why-halo"></div>
  <div class="why-photo" role="img" aria-label="Photo of a consultant working at a laptop in a modern office"></div>

  <div class="why-item" style="left:460px;top:297px"><svg width="40" height="40" viewBox="0 0 40 40"><path d="M20 4l14 8v16l-14 8-14-8V12z M6 12l14 8 14-8M20 20v16" stroke="#fff" stroke-width="2.5" fill="none"/></svg></div>
  <div class="why-label" style="left:346px;top:332px;width:100px;text-align:right">Products</div>

  <div class="why-item" style="left:650px;top:293px"><svg width="40" height="40" viewBox="0 0 40 40"><circle cx="20" cy="16" r="8" stroke="#fff" stroke-width="2.5" fill="none"/><path d="M6 36a14 14 0 0 1 28 0M8 18v-4a12 12 0 0 1 24 0v4" stroke="#fff" stroke-width="2.5" fill="none"/></svg></div>
  <div class="why-label" style="left:759px;top:326px">Support</div>

  <div class="why-item" style="left:333px;top:393px"><svg width="40" height="40" viewBox="0 0 40 40"><circle cx="20" cy="20" r="7" stroke="#fff" stroke-width="2.5" fill="none"/><path d="M20 4v6M20 30v6M4 20h6M30 20h6" stroke="#fff" stroke-width="2.5"/></svg></div>
  <div class="why-label" style="left:201px;top:430px;width:120px;text-align:right">Experience</div>

  <div class="why-item" style="left:779px;top:387px"><svg width="40" height="40" viewBox="0 0 40 40"><path d="M4 12l16-8 16 8v16l-16 8-16-8z M4 12l16 8 16-8M20 20v16" stroke="#fff" stroke-width="2.5" fill="none"/></svg></div>
  <div class="why-label" style="left:892px;top:424px">Delivery</div>

  <div class="why-item" style="left:276px;top:547px"><svg width="40" height="40" viewBox="0 0 40 40"><circle cx="20" cy="20" r="8" stroke="#fff" stroke-width="2.5" fill="none"/><path d="M20 3v6M20 31v6M3 20h6M31 20h6M8 8l4 4M28 28l4 4M8 32l4-4M28 12l4-4" stroke="#fff" stroke-width="2.5"/></svg></div>
  <div class="why-label" style="left:146px;top:582px;width:120px;text-align:right">Approach</div>

  <div class="why-item" style="left:826px;top:540px"><svg width="40" height="40" viewBox="0 0 40 40"><circle cx="20" cy="20" r="15" stroke="#fff" stroke-width="2.5" fill="none"/><path d="M25 14h-7a3 3 0 0 0 0 6h4a3 3 0 0 1 0 6h-7M20 10v4M20 26v4" stroke="#fff" stroke-width="2.5" fill="none"/></svg></div>
  <div class="why-label" style="left:945px;top:577px">Pricing</div>
</section>

<section class="about">
  <div class="about-photo" role="img" aria-label="Photo of a business team meeting around a conference table with laptops"></div>
  <div class="about-card">
    <div class="about-heading">
      <span class="heading-title">ABOUT US</span>
      <span class="heading-sub">WHO WE ARE</span>
    </div>
    <p class="about-text">Lorem ipsum dolor sit amet, conse ctetur adipiscing elit, sed do eiusmod tempor incididunt ut labore et dolore magna aliqua. Ut enim ad minim veniam, quis nostrud exercitation ullamco laboris nisi ut aliquip ex ea commodo consequat</p>
    <a class="btn btn-solid">KNOW MORE
      <svg width="30" height="14" viewBox="0 0 30 14"><path d="M0 7h27M21 1l6 6-6 6" stroke="#fff" stroke-width="2" fill="none"/></svg></a>
  </div>
</section>

<section class="cta" role="img" aria-label="Blue-tinted photo of colleagues collaborating at laptops">
  <h2>DIGITALLY TRANSFORM &amp; GROW YOUR BUSINESS</h2>
  <h3>WANT TO WORK WITH US?</h3>
  <p>Lorem ipsum dolor sit amet, conse ctetur adipiscing elit, sed do eiusmod tempor incididunt ut labore et dolore magna aliqua. Ut enim ad minim veniam, quis nostrud exercitation ullamco laboris nisi ut aliquip ex ea commodo consequat</p>
  <a class="btn btn-outline">CONTACT US
    <svg width="30" height="14" viewBox="0 0 30 14"><path d="M0 7h27M21 1l6 6-6 6" stroke="#fff" stroke-width="2" fill="none"/></svg></a>
</section>

<section class="testimonials">
  <div class="heading" style="top:182px"><div class="heading-inner">
    <span class="heading-title">TESTIMONIALS</span>
    <span class="heading-sub">CLIENT REVIEWS</span>
  </div></div>

  <div class="t-card" style="left:74px">
    <div class="t-avatar" role="img" aria-label="Client portrait"></div>
    <div class="t-quote">&ldquo;</div>
    <p class="t-text">Lorem ipsum dolor sit amet, conse ctetuer adipiscing elit. Aenean comodo ligula eget dolor. Aenean massa. Cum sociis</p>
    <div class="t-rule"></div>
    <div class="t-name">Daniel Harper</div><div class="t-role">Managing Director</div>
    <div class="t-stars">★★★★★</div>
  </div>
  <div class="t-card" style="left:440px">
    <div class="t-avatar" role="img" aria-label="Client portrait"></div>
    <div class="t-quote">&ldquo;</div>
    <p class="t-text">Lorem ipsum dolor sit amet, conse ctetuer adipiscing elit. Aenean comodo ligula eget dolor. Aenean massa. Cum sociis</p>
    <div class="t-rule"></div>
    <div class="t-name">Daniel Harper</div><div class="t-role">Managing Director</div>
    <div class="t-stars">★★★★★</div>
  </div>
  <div class="t-card" style="left:804px">
    <div class="t-avatar" role="img" aria-label="Client portrait"></div>
    <div class="t-quote">&ldquo;</div>
    <p class="t-text">Lorem ipsum dolor sit amet, conse ctetuer adipiscing elit. Aenean comodo ligula eget dolor. Aenean massa. Cum sociis</p>
    <div class="t-rule"></div>
    <div class="t-name">Daniel Harper</div><div class="t-role">Managing Director</div>
    <div class="t-stars">★★★★★</div>
  </div>

  <span class="dot" style="left:569px"></span>
  <span class="dot" style="left:593px"></span>
  <span class="dot on" style="left:618px"></span>
</section>

<footer class="site-footer">
  <div class="f-brand"><span class="brand-dot"></span>BRIDGEMONT</div>
  <span class="f-social" style="left:121px" aria-label="Social link"></span>
  <span class="f-social" style="left:160px" aria-label="Social link"></span>
  <span class="f-social" style="left:199px" aria-label="Social link"></span>
  <span class="f-social" style="left:238px" aria-label="Social link"></span>

  <div class="f-title" style="left:395px">QUICK LINKS</div>
  <ul class="f-links"><li>Home</li><li>Services</li><li>About</li><li>Blog</li><li>Contact Us</li></ul>

  <div class="f-title" style="left:603px">CONTACT US</div>
  <div class="f-contact" style="top:188px"><span class="f-ico"><svg width="12" height="12" viewBox="0 0 12 12"><path d="M2 1l2 0 1 3-1.5 1a6 6 0 0 0 3 3L8 6.5l3 1v2.5A1 1 0 0 1 10 11 9 9 0 0 1 1 2a1 1 0 0 1 1-1z" fill="#0aa2dc"/></svg></span><div>CALL US<br>8012 555 0147</div></div>
  <div class="f-contact" style="top:237px"><span class="f-ico"><svg width="12" height="10" viewBox="0 0 12 10"><rect x=".5" y=".5" width="11" height="9" fill="none" stroke="#0aa2dc"/><path d="M.5 .5l5.5 5 5.5-5" fill="none" stroke="#0aa2dc"/></svg></span><div>EMAIL US<br>info@bridgemontgrp.com</div></div>
  <div class="f-contact" style="top:286px"><span class="f-ico"><svg width="10" height="13" viewBox="0 0 10 13"><path d="M5 13S0 7.5 0 5a5 5 0 0 1 10 0c0 2.5-5 8-5 8z" fill="#0aa2dc"/><circle cx="5" cy="5" r="1.8" fill="#3a3a3c"/></svg></span><div>Address line Dummy Here<br>Address line Here</div></div>

  <div class="f-title" style="left:894px;top:118px">OUR NEWSLETTER</div>
  <p class="f-news">Subscribe our newsletter to get the latest news.</p>
  <div class="f-input">Enter Email Address<span></span></div>
</footer>
<div class="copyright">Copyright © 2024 All Rights Reserved By Company name</div>

</body>
</html>
```